Global social media analytics company needs business card design

We need an updated business card design to align with our new website - brightquillo.net -

I would also like a favicon designed as well.

Target Market(s)

CEOs, CMOs go big companies

Industry/Entity Type

Business

Contact Information for Business Card

Room for the following:
Address
Main telephone
Direct telephone or cell phone
twitter handle

Colors
aaaaaa

Requirements
Must have
• Attention to detail; style.
• Use the logo color from our website - which is gray

```html
<!DOCTYPE html>
<html lang="en">
<head>
<meta charset="utf-8">
<title>brightquillo stationery</title>
<link rel="stylesheet" href="https://fonts.googleapis.com/css2?family=Questrial&display=swap">
<style>
  :root {
    --backdrop: #d6d6d6;
    --paper: #ffffff;
    --brand-gray: #3d3d3d;
    --ink: #333333;
    --ink-on-dark: #ffffff;
    --divider: #555555;
    --faint-mark: #f1f1f1;
  }
  * { box-sizing: border-box; margin: 0; padding: 0; }
  html, body { width: 1200px; height: 1061px; overflow: hidden; }
  body {
    background: var(--backdrop);
    font-family: "Questrial", "Helvetica Neue", Arial, sans-serif;
    color: var(--ink);
    position: relative;
  }
  .sheet, .card {
    position: absolute;
    background: var(--paper);
    box-shadow: 0 2px 6px rgba(0,0,0,.18);
    overflow: hidden;
  }
  .brand { display: flex; align-items: center; gap: 8px; color: var(--brand-gray); }
  .brand-dot { border-radius: 50%; background: var(--brand-gray); flex: none; }
  .brand-name { letter-spacing: -0.01em; }

  /* Letterhead, centred mark */
  .letterhead-centered { left: 100px; top: 100px; width: 460px; height: 610px; }
  .letterhead-centered .brand { position: absolute; top: 22px; left: 0; right: 0; justify-content: center; }
  .letterhead-centered .brand-dot { width: 22px; height: 22px; }
  .letterhead-centered .brand-name { font-size: 15px; }
  .letterhead-footer {
    position: absolute; right: 110px; bottom: 20px;
    display: flex; font-size: 8px; line-height: 1.35;
  }
  .letterhead-footer .address { text-align: right; padding-right: 8px; border-right: 1px solid var(--divider); }
  .letterhead-footer .contact { padding-left: 8px; }

  /* Business card, white side */
  .card-front { left: 686px; top: 76px; width: 404px; height: 178px; display: flex; align-items: center; }
  .card-front .brand { flex-direction: column; width: 132px; gap: 10px; }
  .card-front .brand-dot { width: 70px; height: 70px; }
  .card-front .brand-name { font-size: 14px; }
  .card-front .details {
    border-left: 1px solid var(--divider); height: 150px; padding-left: 14px;
    font-size: 16px; line-height: 1.3; display: flex; flex-direction: column; justify-content: center; gap: 16px;
  }

  /* Business card, dark side */
  .card-back { left: 134px; top: 759px; width: 388px; height: 214px; background: var(--brand-gray); color: var(--ink-on-dark); }
  .card-back .brand { position: absolute; left: 20px; top: 30px; color: var(--ink-on-dark); gap: 14px; }
  .card-back .brand-dot { width: 70px; height: 70px; background: var(--ink-on-dark); }
  .card-back .brand-name { font-size: 38px; }
  .card-back .details { position: absolute; left: 20px; right: 20px; bottom: 20px; display: flex; font-size: 13px; line-height: 1.3; }
  .card-back .details .address { width: 222px; }

  /* Letterhead, corner mark */
  .letterhead-corner { left: 656px; top: 362px; width: 456px; height: 608px; }
  .letterhead-corner .brand { position: absolute; left: 16px; top: 14px; }
  .letterhead-corner .brand-dot { width: 26px; height: 26px; }
  .letterhead-corner .brand-name { font-size: 15px; }
  .letterhead-corner .faint-circle { position: absolute; right: -70px; top: 70px; width: 470px; height: 470px; border-radius: 50%; background: var(--faint-mark); }
</style>
</head>
<body>
  <section class="sheet letterhead-centered">
    <div class="brand"><span class="brand-dot"></span><span class="brand-name">brightquillo</span></div>
    <footer class="letterhead-footer">
      <div class="address">2215 Alder Crest Ave. 4th Fl<br>Fairhaven, MA 02719<br>USA</div>
      <div class="contact">T: +1 555 302 7190<br>E: info@brightquillo.net</div>
    </footer>
  </section>

  <section class="card card-front">
    <div class="brand"><span class="brand-dot"></span><span class="brand-name">brightquillo</span></div>
    <div class="details">
      <div>2215 Alder Crest Ave. 4th Fl<br>Fairhaven, MA 02719<br>USA</div>
      <div>T: +1 555 302 7190<br>E: info@brightquillo.net</div>
    </div>
  </section>

  <section class="card card-back">
    <div class="brand"><span class="brand-dot"></span><span class="brand-name">brightquillo</span></div>
    <div class="details">
      <div class="address">2215 Alder Crest Ave. 4th Fl<br>Fairhaven, MA 02719<br>USA</div>
      <div>T: +1 555 302 7190<br>E: info@brightquillo.net</div>
    </div>
  </section>

  <section class="sheet letterhead-corner">
    <div class="faint-circle"></div>
    <div class="brand"><span class="brand-dot"></span><span class="brand-name">brightquillo</span></div>
  </section>
</body>
</html>
```